Header and footer for report

We would like a header and footer for our building management reports that incorporate a modern city skyline and our logo.

As well as update our other stationery.

```html
<!DOCTYPE html>
<html lang="en">
<head>
<meta charset="utf-8">
<title>Torvane Group Stationery</title>
<link rel="stylesheet" href="https://fonts.googleapis.com/css2?family=PT+Sans+Narrow:wght@400;700&family=PT+Sans:wght@400;700&display=swap">
<style>
  :root {
    --backdrop: #d1d3d4;
    --paper: #ffffff;
    --brand-blue: #1b63ab;
    --brand-blue-deep: #15508f;
    --brand-dark: #073440;
    --soft-grey: #dcdddf;
    --text-grey: #8a8a8a;
    --contact-grey: #555555;
    --skyline-grey: #e6e7e8;
  }
  html, body {
    margin: 0;
    padding: 0;
    width: 1200px;
    height: 1192px;
    overflow: hidden;
    background: var(--backdrop);
  }
  .canvas {
    position: relative;
    width: 1200px;
    height: 1192px;
    background: var(--backdrop);
    font-family: "PT Sans", sans-serif;
  }
  .sheet {
    position: absolute;
    background: var(--paper);
    overflow: hidden;
    box-shadow: 2px 3px 6px rgba(0,0,0,0.18);
  }
  .sheet > svg.art {
    position: absolute;
    left: 0;
    top: 0;
  }
  .brand-name {
    position: absolute;
    margin: 0;
    font-family: "PT Sans Narrow", sans-serif;
    font-weight: 700;
    color: var(--brand-blue);
    letter-spacing: 0.04em;
    white-space: nowrap;
    line-height: 1;
  }

  /* Letterhead */
  .letterhead { left: 83px; top: 59px; width: 485px; height: 680px; }
  .letterhead .brand-name { left: 54px; top: 92px; font-size: 23px; }
  .letterhead .sender {
    position: absolute;
    left: 315px;
    top: 60px;
    width: 112px;
    font-size: 6.6px;
    line-height: 6.8px;
    color: var(--text-grey);
  }
  .letterhead .sender strong { display: block; margin-bottom: 5px; color: #7a7a7a; }
  .letterhead .report-body {
    position: absolute;
    left: 57px;
    top: 181px;
    width: 377px;
    color: var(--text-grey);
  }
  .report-body h2 {
    margin: 0 0 7px;
    font-size: 8.5px;
    font-weight: 700;
    color: #6f6f6f;
    letter-spacing: 0.03em;
  }
  .report-body p {
    margin: 0 0 9px;
    font-size: 7.4px;
    line-height: 9.5px;
  }
  .report-body h2.second { margin-top: 22px; }

  .footer-contacts {
    position: absolute;
    left: 0;
    top: 608px;
    width: 485px;
    height: 40px;
  }
  .contact-item {
    position: absolute;
    top: 0;
    color: #ffffff;
    font-size: 6.4px;
    line-height: 7.6px;
  }
  .contact-item svg { position: absolute; left: -21px; top: 0; }
  .contact-item strong { display: block; margin-bottom: 4px; font-size: 6.8px; }
  .contact-web { left: 90px; }
  .contact-office { left: 218px; }
  .contact-phone { left: 350px; }

  /* Business card front */
  .card-front { left: 685px; top: 188px; width: 375px; height: 220px; }
  .card-front .brand-name { left: 0; width: 375px; text-align: center; top: 131px; font-size: 25px; padding-left: 18px; box-sizing: border-box; }

  /* Business card back */
  .card-back { left: 682px; top: 474px; width: 375px; height: 220px; }
  .card-back .brand-name { right: 27px; top: 83px; font-size: 20px; }
  .card-back .contact-lines {
    position: absolute;
    right: 27px;
    top: 127px;
    margin: 0;
    text-align: right;
    font-family: "PT Sans Narrow", sans-serif;
    font-size: 14.5px;
    line-height: 20.5px;
    color: var(--contact-grey);
  }

  /* Envelope */
  .envelope { left: 80px; top: 814px; width: 506px; height: 308px; background: transparent; }
  .envelope .brand-name { right: 40px; top: 130px; font-size: 21px; }

  /* Standalone brand name */
  .brand-standalone {
    position: absolute;
    left: 700px;
    top: 983px;
    width: 345px;
    text-align: center;
  }
  .brand-standalone .brand-name { position: static; font-size: 40px; }
</style>
</head>
<body>
<main class="canvas">

  <!-- Report letterhead -->
  <section class="sheet letterhead">
    <svg class="art" width="485" height="680" viewBox="0 0 485 680">
      <defs>
        <linearGradient id="lh-footer" x1="0" y1="0" x2="0" y2="1">
          <stop offset="0" stop-color="#ffffff"/>
          <stop offset="0.25" stop-color="var(--soft-grey)"/>
          <stop offset="0.45" stop-color="var(--brand-blue)"/>
          <stop offset="1" stop-color="var(--brand-blue-deep)"/>
        </linearGradient>
      </defs>
      <rect x="0" y="470" width="485" height="210" fill="url(#lh-footer)" role="img" aria-label="Curved blue and grey footer band with city skyline"/>
    </svg>

    <h1 class="brand-name">TORVANE GROUP</h1>

    <div class="sender">
      <strong>Project Report</strong>
      Level 3, 18 Harbour Road<br>
      Sample City 2000<br>
      Ref: BM-2024-017<br>
      Date: 12 March 2024
    </div>

    <article class="report-body">
      <h2>Monthly Building Management Summary</h2>
      <p>This report summarises building operations for the period, including maintenance works completed, scheduled inspections, tenant requests and energy use across all managed sites. Overall performance remained within agreed service levels, with minor delays on two lift servicing visits now resolved. Further detail on each area is provided in the sections that follow.</p>
      <p>Fire safety checks, cleaning audits and security patrols were completed as planned. Any outstanding actions are listed with owners and due dates in the appendix.</p>
      <h2 class="second">Maintenance and Works Overview for the Quarter</h2>
      <p>Planned maintenance covered air conditioning filters, roof drainage, emergency lighting and hot water systems at each property. Reactive jobs fell compared with last quarter, largely due to earlier plant checks and faster contractor response. Two capital projects are under way: the lobby refurbishment at the main tower and the car park lighting upgrade, both on budget. Tenant feedback remains positive, with most requests closed within two working days. Energy use dropped slightly after new controls were fitted to common area lighting. Next quarter we will focus on façade cleaning, lift modernisation planning and a review of waste collection contracts across the portfolio.</p>
    </article>

    <div class="footer-contacts">
      <div class="contact-item contact-web">
        <svg width="12" height="12" viewBox="0 0 12 12"><circle cx="6" cy="6" r="6" fill="#fff"/><circle cx="6" cy="6" r="3.6" fill="none" stroke="var(--brand-blue)" stroke-width="0.9"/><ellipse cx="6" cy="6" rx="1.5" ry="3.6" fill="none" stroke="var(--brand-blue)" stroke-width="0.8"/><line x1="2.4" y1="6" x2="9.6" y2="6" stroke="var(--brand-blue)" stroke-width="0.8"/></svg>
        <strong>Online</strong>
        www.torvanegroup.example<br>
        info@torvanegroup.example
      </div>
      <div class="contact-item contact-office">
        <svg width="12" height="12" viewBox="0 0 12 12"><circle cx="6" cy="6" r="6" fill="#fff"/><path d="M3,6.2 L6,3.3 L9,6.2 L8.2,6.2 L8.2,8.8 L3.8,8.8 L3.8,6.2 Z" fill="var(--brand-blue)"/></svg>
        <strong>Office</strong>
        18 Harbour Road<br>
        Sample City 2000
      </div>
      <div class="contact-item contact-phone">
        <svg width="12" height="12" viewBox="0 0 12 12"><circle cx="6" cy="6" r="6" fill="#fff"/><path d="M4,3 L5.2,3 L5.7,4.8 L4.9,5.4 C5.4,6.5 5.9,7 6.9,7.4 L7.5,6.6 L9.1,7.1 L9.1,8.3 C6.2,8.6 3.5,6 4,3 Z" fill="var(--brand-blue)"/></svg>
        <strong>Call us</strong>
        +1 555 0100<br>
        +1 555 0101
      </div>
    </div>
  </section>

  <!-- Business card, front -->
  <section class="sheet card-front">
    <svg class="art" width="375" height="220" viewBox="0 0 375 220">
      <defs>
        <linearGradient id="card-skyline" x1="0" y1="0" x2="0" y2="1">
          <stop offset="0" stop-color="var(--skyline-grey)" stop-opacity="0"/>
          <stop offset="0.5" stop-color="var(--skyline-grey)" stop-opacity="0.7"/>
          <stop offset="1" stop-color="var(--skyline-grey)" stop-opacity="1"/>
        </linearGradient>
      </defs>
      <rect x="0" y="75" width="375" height="145" fill="url(#card-skyline)" role="img" aria-label="Faint city skyline silhouette"/>
    </svg>
    <h2 class="brand-name">TORVANE GROUP</h2>
  </section>

  <!-- Business card, back -->
  <section class="sheet card-back">
    <svg class="art" width="375" height="220" viewBox="0 0 375 220">
      <defs>
        <linearGradient id="card-band" x1="0" y1="0" x2="1" y2="0">
          <stop offset="0" stop-color="var(--brand-blue)"/>
          <stop offset="0.7" stop-color="var(--brand-blue-deep)"/>
          <stop offset="1" stop-color="var(--soft-grey)"/>
        </linearGradient>
      </defs>
      <rect x="0" y="0" width="150" height="220" fill="url(#card-band)" role="img" aria-label="Curved blue and grey swoosh panel"/>
    </svg>
    <h2 class="brand-name">TORVANE GROUP</h2>
    <p class="contact-lines">
      Phone: +1 555 0100<br>
      Adress: Your City&nbsp; Your adress<br>
      Mail: hello@torvanegroup.example
    </p>
  </section>

  <!-- Envelope -->
  <section class="sheet envelope">
    <svg class="art" width="506" height="308" viewBox="0 0 506 308">
      <defs>
        <linearGradient id="env-band" x1="0" y1="0" x2="0" y2="1">
          <stop offset="0" stop-color="#ffffff"/>
          <stop offset="0.2" stop-color="var(--soft-grey)"/>
          <stop offset="0.45" stop-color="var(--brand-blue)"/>
          <stop offset="1" stop-color="var(--brand-blue-deep)"/>
        </linearGradient>
      </defs>
      <rect x="0" y="56" width="506" height="252" fill="var(--paper)"/>
      <path d="M9,0 L497,0 Q503,0 504,6 L506,56 L0,56 L4,6 Q5,0 9,0 Z" fill="var(--brand-dark)"/>
      <rect x="0" y="165" width="506" height="143" fill="url(#env-band)" role="img" aria-label="Curved blue and grey band with city skyline"/>
    </svg>
    <h2 class="brand-name">TORVANE GROUP</h2>
  </section>

  <!-- Standalone brand name -->
  <div class="brand-standalone">
    <h2 class="brand-name">TORVANE GROUP</h2>
  </div>

</main>
</body>
</html>
```